Flyer-Design für Österreichische Bienen-Aktie
Super so wie ich es mir vorgestellt habe!!!
Zielgruppe
Firma FlorWerk
Zielgruppe ist jeder der sich mit Umweltschutz / Nachhaltigkeit / BIO ausseinandersetzt.
Aufgabenstellung
Das Format ist DinLang
Datenformat (inkl. 2,00 mm Beschnitt): 21,40 x 21,40 cm
Endformat (offen): 21,00 x 21,00 cm
Endformat (geschlossen): 10,50 x 21,00 cm
Was soll am Flyer stehen.
Die Stilrichtung in Richtung ÖKO bitte
Erste Österreichische Bienen-Aktie
Noch nie schmeckte Ihnen Ihr Investment so gut.
Kosten pro Aktie 250,-- exkl. MwSt.
was bekommt man 5 Jahre lang 3,5 Kg Honig ergibt mit dem Heutigem Honigpreis von 14,90 je kg am Ende der Laufzeit 260,75€
Mit Ihrem Engagement sichern Sie Tausenden dieser wundervollen Nützlinge das Überleben und ermöglichen eine intensive und nachhaltige Betreuung durch FlorWerk.
Was wird mit dem Geld gemacht?
Zum einen werden Bienenvölker zugekauft zum anderen wird in sogenannte Bienenoasen Investiert.
Bienenoasen sind Rückzugsgebiete in denen sich alle Insekten erholen können. Wie sehen solche Oasen aus? Ein kleiner Vorgeschmack unter https://www.videoportal-beispiel.de/watch?v=qR_8TL-ZP2N
Auf diesen Bienenoasen werden Blumen Bäume und Sträucher gesetzt die als Nahrungsgrundlage für alle bestäubenden Insekten dienen.
Ihre Dividende (Honig)
Die Honiggläser werden individuell gebrandet Sprich sie können den Honig weiterschenken oder auch gerne Selber Essen. Es ist vieles Möglich Logo / Texte / Fotos können am Honigglas angebracht werden. Für Firmen gegen Aufpreis ist das abfüllen in vielen Kleingläser möglich = Ideale Werbung!

```html
<!DOCTYPE html>
<html lang="de">
<head>
<meta charset="utf-8">
<title>Erste Österreichische ImkerAnteil – Flyer</title>
<link rel="stylesheet" href="https://fonts.googleapis.com/css2?family=Cinzel:wght@400;700&display=swap">
<style>
  :root {
    --page: #ffffff;
    --ink-light: #f4ece4;
    --ink-dark: #1c1a1a;
    --amber: #b4581c;
    --ember: #d8431c;
    --strip: rgba(8, 5, 3, 0.78);
  }
  * { margin: 0; padding: 0; box-sizing: border-box; }
  html, body { width: 1200px; height: 670px; overflow: hidden; background: var(--page); }
  body { position: relative; font-family: "Cinzel", serif; color: var(--ink-light); }

  /* ---------- Cover (closed front) ---------- */
  .cover {
    position: absolute; left: 0; top: 0; width: 474px; height: 474px; overflow: hidden;
    border-bottom: 2px solid var(--amber);
  }
  .cover__photo {
    position: absolute; inset: 0;
    background:
      radial-gradient(ellipse 120px 110px at 270px 170px, rgba(180, 100, 50, 0.75), transparent 75%),
      radial-gradient(ellipse 200px 120px at 230px 390px, rgba(220, 70, 30, 0.9), transparent 80%),
      linear-gradient(180deg, #120c08 0%, #2a1a10 45%, #7a2410 65%, #b8361a 82%, #6e2410 100%);
  }
  .cover__strip {
    position: absolute; left: 370px; top: 0; width: 104px; height: 474px; background: var(--strip);
  }
  .cover__title {
    position: absolute; left: 386px; top: 449px;
    transform: rotate(-90deg); transform-origin: 0 0;
    white-space: nowrap; line-height: 1; font-weight: 400;
  }
  .cover__title-small { display: block; font-size: 19px; letter-spacing: 7.5px; margin-bottom: 7px; }
  .cover__title-large { display: block; font-size: 40px; letter-spacing: 10px; }
  .cover__contact {
    position: absolute; left: 19px; width: 200px; top: 362px;
    text-align: center; font-size: 7.5px; line-height: 14px; font-style: normal;
  }

  /* ---------- Inner page ---------- */
  .inner {
    position: absolute; left: 487px; top: 0; width: 474px; height: 474px; overflow: hidden;
    background:
      radial-gradient(ellipse 160px 120px at 300px 180px, rgba(120, 70, 35, 0.55), transparent 75%),
      radial-gradient(ellipse 300px 160px at 260px 420px, rgba(110, 45, 15, 0.55), transparent 80%),
      linear-gradient(180deg, #0d0907 0%, #1c120b 40%, #2a160a 75%, #1a0d06 100%);
  }
  .inner__tagline {
    position: absolute; left: 26px; top: 48px; font-size: 9.5px; line-height: 11.5px;
  }
  .inner__title-band {
    position: absolute; left: 0; top: 87px; width: 336px; height: 64px; background: var(--page);
    color: var(--ink-dark); padding: 19px 0 0 23px;
  }
  .inner__title-small { display: block; font-size: 12px; letter-spacing: 3.8px; line-height: 1; }
  .inner__title-large { display: block; font-size: 25px; letter-spacing: 4.3px; line-height: 1; margin-top: 3px; }
  .inner__photo {
    position: absolute; left: 336px; top: 0; width: 128px; height: 173px;
    background:
      radial-gradient(ellipse 40px 40px at 60px 70px, rgba(190, 110, 50, 0.85), transparent 80%),
      linear-gradient(180deg, #1a100a 0%, #5a2a12 45%, var(--ember) 75%, #7a2010 100%);
  }
  .inner__column {
    position: absolute; top: 208px; width: 206px; font-size: 6.8px; line-height: 10.9px;
    letter-spacing: -0.05px;
  }
  .inner__column--left { left: 22px; }
  .inner__column--right { left: 251px; }
  .facts { display: grid; grid-template-columns: 77px 1fr; margin-bottom: 10.9px; }
  .facts dt { font-weight: 700; }
  .heading { font-size: 9.2px; font-weight: 700; line-height: 12px; margin-top: 8px; }
  .inner__column--right .heading { margin-top: 5px; }
  .link { word-break: break-all; }
</style>
</head>
<body>

  <section class="cover">
    <div class="cover__photo" role="img" aria-label="Nahaufnahme einer Biene auf einer roten Blüte"></div>
    <div class="cover__strip"></div>
    <h1 class="cover__title">
      <span class="cover__title-small">Erste&nbsp; Österreichische</span>
      <span class="cover__title-large">ImkerAnteil</span>
    </h1>
    <address class="cover__contact">
      FlorWerk<br>
      Honigland Mitte GmbH<br>
      Lindenweg 24<br>
      7000 Wiesenfeld<br>
      kontakt@florwerk.at
    </address>
  </section>

  <section class="inner">
    <p class="inner__tagline">Noch nie schmeckte Ihnen<br>Ihr Investment so gut.</p>

    <div class="inner__title-band">
      <span class="inner__title-small">Erste&nbsp; Österreichische</span>
      <span class="inner__title-large">ImkerAnteil</span>
    </div>

    <div class="inner__photo" role="img" aria-label="Biene auf einer orangeroten Blüte"></div>

    <div class="inner__column inner__column--left">
      <dl class="facts">
        <dt>Kosten pro Aktie:</dt><dd>250,-- exkl. MwSt.</dd>
        <dt>was bekommt man:</dt><dd>5 Jahre lang 3,5 Kg Honig</dd>
      </dl>
      <p>ergibt mit dem Heutigem Honigpreis von 14,90 je kg am Ende der Laufzeit 260,75€</p>
      <p>Mit Ihrem Engagement sichern Sie Tausenden dieser wundervollen Nützlinge das Überleben und ermöglichen eine intensive und nachhaltige Betreuung durch FlorWerk.</p>
      <h2 class="heading">Was wird mit dem Geld gemacht?</h2>
      <p>Zum einen werden Bienenvölker zugekauft zum anderen wird in sogenannte Bienenoasen Investiert. Bienenoasen sind Rückzugsgebiete in denen sich alle</p>
    </div>

    <div class="inner__column inner__column--right">
      <p>Insekten erholen können. Wie sehen solche Oasen aus? Ein kleiner Vorgeschmack unter <span class="link">https://www.videoportal-beispiel.de/watch?v=qR_8TL-ZP2N</span></p>
      <p>Auf diesen Bienenoasen werden Blumen Bäume und Sträucher gesetzt die als Nahrungsgrundlage für alle bestäubenden Insekten dienen.</p>
      <h2 class="heading">Ihre Dividende (Honig)</h2>
      <p>Die Honiggläser werden individuell gebrandet Sprich sie können den Honig weiterschenken oder auch gerne Selber Essen. Es ist vieles Möglich Logo / Texte / Fotos können am Honigglas angebracht werden. Für Firmen gegen Aufpreis ist das abfüllen in vielen Kleingläser möglich = Ideale Werbung!</p>
    </div>
  </section>

</body>
</html>
```